Property Management Company Business Cards

Need business cards for a property management company located in Michigan. We manage houses for clients all over the world. Young and modern company, looking for eye catching design. Please work with the attached logo.

Industry/Entity Type

Property Management

Requirements
Must have
• Need lines for address, telephone number, fax number, web site.

Also lines for name, and job title

```html
<!DOCTYPE html>
<html lang="en">
<head>
<meta charset="utf-8">
<title>Lakeshore Harbor Management – Business Cards</title>
<link href="https://fonts.googleapis.com/css2?family=Open+Sans:wght@400;700&display=swap" rel="stylesheet">
<style>
  :root {
    --page: #d9d9d9;
    --card: #f7f7f7;
    --panel: #e9e9e8;
    --blue: #2aa3d8;
    --ink: #333538;
    --white: #ffffff;
  }
  html, body {
    margin: 0;
    width: 1200px;
    height: 1046px;
    overflow: hidden;
    background: var(--page);
    font-family: "Open Sans", Arial, sans-serif;
  }
  .sheet { position: relative; width: 1200px; height: 1046px; }

  .card {
    position: absolute;
    left: 250px;
    width: 700px;
    height: 400px;
    overflow: hidden;
    box-shadow: 0 6px 18px rgba(0,0,0,0.18);
  }

  /* Back of card */
  .card--back { top: 90px; background: var(--blue); }
  .card--back .panel {
    position: absolute;
    left: 46px; right: 46px; top: 34px; bottom: 78px;
    background: var(--panel);
  }
  .card--back .rule-v {
    position: absolute; top: 0; bottom: 0; width: 5px; background: var(--ink);
  }
  .card--back .rule-v--left { left: 41px; }
  .card--back .rule-v--right { right: 41px; }
  .card--back .rule-h {
    position: absolute; left: 41px; right: 41px; height: 5px; background: var(--ink);
  }
  .card--back .rule-h--top { top: 29px; }
  .card--back .rule-h--bottom { bottom: 73px; }
  .card--back .brand {
    position: absolute; left: 0; right: 0; top: 90px;
    display: flex; flex-direction: column; align-items: center; gap: 14px;
  }
  .brand-dot {
    display: block; border-radius: 50%; background: var(--blue);
  }
  .card--back .brand-dot { width: 74px; height: 74px; }
  .brand-name {
    color: var(--ink); font-weight: 700; text-transform: uppercase;
    line-height: 1.05; text-align: center;
  }
  .card--back .brand-name { font-size: 30px; letter-spacing: 0.5px; }
  .brand-name .sub { display: block; font-size: 0.55em; letter-spacing: 0.55em; }

  /* Front of card */
  .card--front { top: 556px; background: var(--card); }
  .card--front .brand {
    position: absolute; left: 30px; top: 24px;
    display: flex; align-items: center; gap: 12px;
  }
  .card--front .brand-dot { width: 40px; height: 40px; }
  .card--front .brand-name { font-size: 20px; text-align: left; }

  .person { position: absolute; left: 30px; top: 92px; color: var(--blue); }
  .person-name { margin: 0; font-size: 46px; font-weight: 400; line-height: 1; }
  .person-title { margin: 4px 0 0 82px; font-size: 24px; font-weight: 400; line-height: 1; }

  .contact {
    position: absolute; left: 30px; top: 196px;
    color: var(--blue); font-size: 16px; line-height: 1.35;
  }
  .contact p { margin: 0; }

  .house-photo {
    position: absolute; right: 34px; top: 104px;
    width: 250px; height: 220px;
    background: linear-gradient(160deg, #5a5d62 0%, #5a5d62 28%, #36a7da 30%, #2590c4 100%);
    border-radius: 4px;
  }

  .band {
    position: absolute; left: 0; right: 0; bottom: 0; height: 68px;
    background: var(--blue);
    border-top: 5px solid var(--ink);
    color: var(--white); font-size: 20px;
    display: flex; justify-content: space-between; align-items: center;
    padding: 0 30px; box-sizing: border-box;
  }
</style>
</head>
<body>
<main class="sheet">

  <section class="card card--back" aria-label="Business card back">
    <div class="panel"></div>
    <span class="rule-v rule-v--left"></span>
    <span class="rule-v rule-v--right"></span>
    <span class="rule-h rule-h--top"></span>
    <span class="rule-h rule-h--bottom"></span>
    <div class="brand">
      <span class="brand-dot"></span>
      <div class="brand-name">Lakeshore Harbor<span class="sub">Management</span></div>
    </div>
  </section>

  <section class="card card--front" aria-label="Business card front">
    <div class="brand">
      <span class="brand-dot"></span>
      <div class="brand-name">Lakeshore Harbor<span class="sub">Management</span></div>
    </div>

    <div class="person">
      <h1 class="person-name">John Doe</h1>
      <h2 class="person-title">Job Title</h2>
    </div>

    <div class="contact">
      <p>1234 Address Lane</p>
      <p>City, State, Zip</p>
      <p>P: 555-555-555 &bull; F: 555-555-555</p>
    </div>

    <div class="house-photo" role="img" aria-label="Illustration of a blue two-storey house with a grey roof"></div>

    <div class="band">
      <span class="website">www.example-homes.com</span>
      <span class="email">me@example-homes.com</span>
    </div>
  </section>

</main>
</body>
</html>
```